Pitch deck for fundraising for a timber drying business

We have the basic content in a powerpoint but need someone to take that and make an attractive and engaging document for a reader who may see hundreds of these a week so visual impact is key.
We are launching a timber drying business in Australia using an exclusive line of kilns not otherwise available in Australia.
Designs should focus on natural tones and connections with forests and timber, probably with a green (colour) focus.

Target Market(s)

investors, wealthyindividuals

Colors

Designer to choose colors to be used in the design.

Requirements
Nice to have
• Design in Canva or similar

```html
<!DOCTYPE html>
<html lang="en">
<head>
<meta charset="utf-8">
<title>Karridale Kilns Pitch Deck</title>
<link href="https://fonts.googleapis.com/css2?family=Poppins:wght@300;400;600;700;800&family=Raleway:wght@400;500;600&display=swap" rel="stylesheet">
<style>
  :root {
    --teal: #21ad95;
    --teal-bright: #2bbfa4;
    --stage-top: #3e3e3e;
    --stage-bottom: #464646;
    --caption: #5c5c5c;
    --ink: #2a2a2a;
    --paper: #f6f6f6;
    --dark-slide: #1d1d1d;
    --white: #ffffff;
  }
  * { box-sizing: border-box; margin: 0; padding: 0; }
  html, body { width: 1200px; height: 2520px; overflow: hidden; }
  body {
    position: relative;
    background: linear-gradient(to bottom, var(--stage-top) 0, var(--stage-top) 993px, var(--stage-bottom) 993px, var(--stage-bottom) 100%);
    font-family: "Raleway", Arial, sans-serif;
  }
  .slide { position: absolute; overflow: hidden; box-shadow: 0 6px 14px rgba(0,0,0,.35); }
  .slide-photo { position: absolute; inset: 0; }

  .logs-fill {
    background:
      radial-gradient(circle at 20% 30%, #d39a62 0, transparent 16%),
      radial-gradient(circle at 48% 22%, #e0b88a 0, transparent 14%),
      radial-gradient(circle at 78% 35%, #c98650 0, transparent 15%),
      radial-gradient(circle at 30% 80%, #dcae7d 0, transparent 15%),
      radial-gradient(circle at 65% 78%, #c47f48 0, transparent 16%),
      radial-gradient(circle at 90% 82%, #d7a673 0, transparent 13%),
      linear-gradient(135deg, #8a4f28, #b9773f 45%, #7a4222);
  }
  .cover-band {
    position: absolute; left: 0; right: 0;
    background: linear-gradient(to bottom, rgba(32,18,10,.94), rgba(24,13,7,.96));
    border-top: 2px solid rgba(255,240,225,.75);
    border-bottom: 2px solid rgba(255,240,225,.75);
    text-align: center; color: var(--white);
  }
  .cover-title { font-family: "Poppins", Arial, sans-serif; font-weight: 700; color: var(--teal-bright); letter-spacing: .5px; line-height: 1; white-space: nowrap; }
  .cover-sub { font-family: "Poppins", Arial, sans-serif; font-weight: 300; line-height: 1; }
  .cover-url { font-family: "Raleway", Arial, sans-serif; font-weight: 500; color: #e8e2dc; }

  .hero { left: 195px; top: 186px; width: 818px; height: 613px; }
  .hero .cover-band { top: 234px; height: 186px; }
  .hero .cover-title { font-size: 66px; margin-top: 22px; }
  .hero .cover-sub { font-size: 50px; margin-top: 4px; }
  .hero .cover-url { font-size: 15px; letter-spacing: 6px; margin-top: 12px; }

  .grid-cover { left: 54px; top: 1068px; width: 530px; height: 396px; }
  .grid-cover .cover-band { top: 152px; height: 120px; }
  .grid-cover .cover-title { font-size: 43px; margin-top: 13px; }
  .grid-cover .cover-sub { font-size: 31px; margin-top: 3px; }
  .grid-cover .cover-url { font-size: 9.5px; letter-spacing: 4px; margin-top: 8px; }

  .samples-cover { left: 608px; top: 1068px; width: 530px; height: 396px; text-align: center; color: var(--white); }
  .samples-fill {
    background:
      linear-gradient(to bottom, rgba(0,0,0,0) 40%, rgba(22,14,10,.9) 72%, #1a110c 100%),
      linear-gradient(100deg, #5c4333 0, #8a6a52 25%, #c97a4c 45%, #e3b48e 58%, #b2713f 70%, #caa080 85%, #6a4b36 100%);
  }
  .samples-cover .cover-title { position: absolute; left: 0; right: 0; top: 284px; font-size: 43px; }
  .samples-cover .cover-sub { position: absolute; left: 0; right: 0; top: 332px; font-size: 31px; }
  .samples-cover .cover-url { position: absolute; left: 0; right: 0; top: 370px; font-size: 9.5px; letter-spacing: 4px; }

  .content-slide { width: 530px; height: 396px; }
  .content-slide.dark { background: var(--dark-slide); color: #e4e4e4; }
  .content-slide.light { background: var(--paper); color: var(--ink); }
  .dark-fill { background: radial-gradient(circle at 30% 20%, #333 0, transparent 30%), radial-gradient(circle at 75% 70%, #2c2c2c 0, transparent 35%), linear-gradient(160deg, #232323, #151515); }
  .light-fill { background: radial-gradient(circle at 25% 30%, #ffffff 0, transparent 30%), radial-gradient(circle at 80% 70%, #ffffff 0, transparent 30%), linear-gradient(160deg, #f1f1f1, #f8f8f8); }
  .accent-rule { position: absolute; left: 34px; top: 0; width: 2px; height: 66px; }
  .dark .accent-rule { background: #ddd; }
  .light .accent-rule { background: #333; }
  .slide-title { position: absolute; left: 45px; top: 50px; font-family: "Poppins", Arial, sans-serif; font-weight: 700; font-size: 24px; color: var(--teal); letter-spacing: .3px; line-height: 1; }
  .slide-body { position: absolute; left: 34px; top: 104px; width: 476px; font-size: 8.6px; line-height: 11px; text-align: justify; }
  .slide-body p { margin-bottom: 10.5px; }
  .slide-footer { position: absolute; left: 34px; bottom: 22px; display: flex; align-items: center; gap: 6px; font-family: "Poppins", Arial, sans-serif; font-weight: 600; font-size: 8.5px; }
  .dark .slide-footer { color: var(--white); }
  .page-num { position: absolute; right: 33px; bottom: 0; width: 23px; height: 39px; background: var(--teal); color: var(--white); font-family: "Poppins", Arial, sans-serif; font-weight: 700; font-size: 11px; display: flex; align-items: center; justify-content: center; }

  .intro { left: 54px; top: 1493px; }
  .model { left: 608px; top: 1493px; }
  .treads { left: 54px; top: 1919px; }
  .market { left: 608px; top: 1919px; }

  .model-lead { position: absolute; left: 34px; top: 103px; width: 450px; font-size: 9px; line-height: 11.5px; }
  .model-wave { position: absolute; left: 0; top: 136px; }
  .step { position: absolute; top: 280px; width: 110px; text-align: center; }
  .step-label { font-size: 8px; line-height: 10px; color: var(--ink); }
  .step-price { font-family: "Poppins", Arial, sans-serif; font-weight: 700; font-size: 16px; color: var(--teal); margin-top: 7px; }

  .tread-list { position: absolute; left: 34px; top: 112px; width: 250px; list-style: none; }
  .tread-list li { display: flex; gap: 8px; font-size: 9px; line-height: 11.5px; margin-bottom: 13px; }
  .tread-list svg { flex: none; margin-top: 1px; }
  .charred-fill { position: absolute; left: 320px; top: 57px; width: 210px; height: 281px; background: linear-gradient(170deg, #3a2a22, #6b3b25 30%, #241b17 55%, #7a4a30 75%, #2a2422); }

  .market .slide-body { top: 106px; }

  .board-caption { position: absolute; left: 0; right: 0; top: 2404px; text-align: center; font-family: "Poppins", Arial, sans-serif; font-weight: 800; font-size: 51px; color: var(--caption); letter-spacing: 1px; }
</style>
</head>
<body>

<section class="slide hero">
  <div class="slide-photo logs-fill" role="img" aria-label="Photograph of stacked cut log ends"></div>
  <div class="cover-band">
    <h1 class="cover-title">KARRIDALE KILNS</h1>
    <p class="cover-sub">PITCH DECK</p>
    <p class="cover-url">www.websiteaddress.com</p>
  </div>
</section>

<section class="slide grid-cover">
  <div class="slide-photo logs-fill" role="img" aria-label="Photograph of stacked cut log ends"></div>
  <div class="cover-band">
    <h2 class="cover-title">KARRIDALE KILNS</h2>
    <p class="cover-sub">PITCH DECK</p>
    <p class="cover-url">www.websiteaddress.com</p>
  </div>
</section>

<section class="slide samples-cover">
  <div class="slide-photo samples-fill" role="img" aria-label="Photograph of fanned timber colour samples on a table"></div>
  <h2 class="cover-title">KARRIDALE KILNS</h2>
  <p class="cover-sub">PITCH DECK</p>
  <p class="cover-url">www.websiteaddress.com</p>
</section>

<section class="slide content-slide dark intro">
  <div class="slide-photo dark-fill" role="img" aria-label="Dark photograph of charred log ends"></div>
  <span class="accent-rule"></span>
  <h2 class="slide-title">INTRODUCTION</h2>
  <div class="slide-body">
    <p>Karridale Kilns International (KKI) has secured exclusive access to a superior timber drying technology (KilnPro kilns) that has been in commercial production since 1980.</p>
    <p>KKI will leverage this technology to build a hardwood drying business, initially focused on the stair tread market in Sydney and Brisbane.</p>
    <p>Hardwood stair tread timber has an approximate gross margin of $XXXX/m3 (XX%).</p>
    <p>KKI will sell directly to stair tread installers enabling us to retain the bulk of the gross margin as net profit.</p>
    <p>KilnPro kilns are relatively inexpensive ($US79-205K), modular in design, and return approximately 300% per annum. As a result, KKI will be able to scale without additional equity or debt funding.</p>
    <p>The Australian hardwood industry is worth around $7bn pa on 700,000m3 of sawn timber but 93% of logs are exported. With 10 kilns KKI would dry less than 1% of all sawn timber but turn over $XXm and nett $XXm with huge growth potential from value adding exported logs.</p>
    <p>This is not a tech play but a cash cow investment to be held long term. We have a simple business model, using established technology to disrupt a technologically stagnant, but growing industry.</p>
  </div>
  <div class="slide-footer">
    <svg width="10" height="10" viewBox="0 0 10 10" aria-hidden="true"><circle cx="5" cy="5" r="4.3" fill="none" stroke="#21ad95" stroke-width="1"/><ellipse cx="5" cy="5" rx="1.8" ry="4.3" fill="none" stroke="#21ad95" stroke-width=".8"/><line x1=".7" y1="5" x2="9.3" y2="5" stroke="#21ad95" stroke-width=".8"/></svg>
    www.websiteaddress.com
  </div>
  <div class="page-num">01</div>
</section>

<section class="slide content-slide light model">
  <div class="slide-photo light-fill" role="img" aria-label="Faint pale photograph of log ends"></div>
  <span class="accent-rule"></span>
  <h2 class="slide-title">BUSINESS MODEL</h2>
  <p class="model-lead">We are using established technology to disrupt the existing timber supply chain with a simple 4 step business model</p>
  <svg class="model-wave" width="530" height="130" viewBox="0 0 530 130">
    <defs>
      <linearGradient id="wave-tone" x1="0" x2="1" y1="0" y2="0">
        <stop offset="0" stop-color="#21ad95"/><stop offset=".5" stop-color="#7fd3c3"/><stop offset="1" stop-color="#21ad95"/>
      </linearGradient>
    </defs>
    <path d="M-4 110 Q18 63 37 63 A55 55 0 0 1 147 63 L152 63 A55 55 0 0 0 262 63 L266 63 A55 55 0 0 1 376 63 L377 63 A55 55 0 0 0 487 63 Q512 63 536 100" fill="none" stroke="url(#wave-tone)" stroke-width="15"/>
    <circle cx="92" cy="63" r="49" fill="#fff"/>
    <circle cx="207" cy="63" r="49" fill="#fff"/>
    <circle cx="321" cy="63" r="49" fill="#fff"/>
    <circle cx="432" cy="63" r="49" fill="#fff"/>
    <circle cx="92" cy="63" r="46" fill="#7a4a2c" role="img" aria-label="Photograph of cut timber stacked at a sawmill"/>
    <circle cx="207" cy="63" r="46" fill="#5a3b26" role="img" aria-label="Photograph of timber loaded inside a kiln"/>
    <circle cx="321" cy="63" r="46" fill="#6d7a86" role="img" aria-label="Photograph of timber being dressed on a machine"/>
    <circle cx="432" cy="63" r="46" fill="#c9a57a" role="img" aria-label="Photograph of finished stair treads stacked"/>
  </svg>
  <div class="step" style="left:37px"><p class="step-label">Buy cut timber<br>from sawmills</p><p class="step-price">$XXX M3</p></div>
  <div class="step" style="left:152px"><p class="step-label">Dry it in<br>our kilns</p><p class="step-price">$XXX M3</p></div>
  <div class="step" style="left:266px"><p class="step-label">Dress and<br>deliver</p><p class="step-price">$XXX M3</p></div>
  <div class="step" style="left:377px"><p class="step-label">Sell dried stair<br>treads to installers</p><p class="step-price">$XXX M3</p></div>
  <div class="slide-footer">
    <svg width="10" height="10" viewBox="0 0 10 10" aria-hidden="true"><circle cx="5" cy="5" r="4.3" fill="none" stroke="#21ad95" stroke-width="1"/><ellipse cx="5" cy="5" rx="1.8" ry="4.3" fill="none" stroke="#21ad95" stroke-width=".8"/><line x1=".7" y1="5" x2="9.3" y2="5" stroke="#21ad95" stroke-width=".8"/></svg>
    www.websiteaddress.com
  </div>
  <div class="page-num">02</div>
</section>

<section class="slide content-slide light treads">
  <div class="slide-photo light-fill" role="img" aria-label="Faint pale photograph of log ends"></div>
  <span class="accent-rule"></span>
  <h2 class="slide-title">WHY STAIR TREADS</h2>
  <ul class="tread-list">
    <li><svg width="10" height="10" viewBox="0 0 10 10" aria-hidden="true"><circle cx="5" cy="5" r="4.3" fill="none" stroke="#21ad95"/><path d="M3 5.2 L4.4 6.5 L7 3.7" fill="none" stroke="#21ad95" stroke-width="1.1"/></svg>XX% margin</li>
    <li><svg width="10" height="10" viewBox="0 0 10 10" aria-hidden="true"><circle cx="5" cy="5" r="4.3" fill="none" stroke="#21ad95"/><path d="M3 5.2 L4.4 6.5 L7 3.7" fill="none" stroke="#21ad95" stroke-width="1.1"/></svg>High absolute $ returns - ~$XXXm3 profit</li>
    <li><svg width="10" height="10" viewBox="0 0 10 10" aria-hidden="true"><circle cx="5" cy="5" r="4.3" fill="none" stroke="#21ad95"/><path d="M3 5.2 L4.4 6.5 L7 3.7" fill="none" stroke="#21ad95" stroke-width="1.1"/></svg>Standardised product allowing optimisation of production processes</li>
    <li><svg width="10" height="10" viewBox="0 0 10 10" aria-hidden="true"><circle cx="5" cy="5" r="4.3" fill="none" stroke="#21ad95"/><path d="M3 5.2 L4.4 6.5 L7 3.7" fill="none" stroke="#21ad95" stroke-width="1.1"/></svg>Large market - over 65 potential clients indicated interest in purchasing in Sydney alone¹</li>
    <li><svg width="10" height="10" viewBox="0 0 10 10" aria-hidden="true"><circle cx="5" cy="5" r="4.3" fill="none" stroke="#21ad95"/><path d="M3 5.2 L4.4 6.5 L7 3.7" fill="none" stroke="#21ad95" stroke-width="1.1"/></svg>Installers looking for alternatives - ~30% of Corvale products out of specification resulting in no installer profit on those jobs</li>
    <li><svg width="10" height="10" viewBox="0 0 10 10" aria-hidden="true"><circle cx="5" cy="5" r="4.3" fill="none" stroke="#21ad95"/><path d="M3 5.2 L4.4 6.5 L7 3.7" fill="none" stroke="#21ad95" stroke-width="1.1"/></svg>Significant drying time advantage over competitors: 1 week v 7-8 months</li>
  </ul>
  <div class="charred-fill" role="img" aria-label="Photograph of charred timber stacked in a pile"></div>
  <div class="slide-footer">
    <svg width="10" height="10" viewBox="0 0 10 10" aria-hidden="true"><circle cx="5" cy="5" r="4.3" fill="none" stroke="#21ad95" stroke-width="1"/><ellipse cx="5" cy="5" rx="1.8" ry="4.3" fill="none" stroke="#21ad95" stroke-width=".8"/><line x1=".7" y1="5" x2="9.3" y2="5" stroke="#21ad95" stroke-width=".8"/></svg>
    www.websiteaddress.com
  </div>
  <div class="page-num">03</div>
</section>

<section class="slide content-slide light market">
  <div class="slide-photo light-fill" role="img" aria-label="Faint pale photograph of log ends"></div>
  <span class="accent-rule"></span>
  <h2 class="slide-title">MARKET OVERVIEW</h2>
  <div class="slide-body">
    <p>The total value of the Australian timber market is $23.9bn¹ with hardwood accounting for over $7bn and softwood the balance. The Australian hardwood market has been growing strongly, posting 10% growth in volume of logs harvested and a 13% increase in price in 2017 despite a 5% fall in housing construction.</p>
    <p>The hardwood industry however is massively under developed with 93%² of all plantation hardwood logs being exported - with no value adding.</p>
    <p>The total volume of sawn hardwood timber in 2018 was 700,000m3. With just 10 kilns we would dry less than 6,800m3 pa, gross $30.6m in revenue and net $18.5m with significant opportunity to expand.</p>
    <p>In NSW logs are sourced through either the State Forestry Board (Owen knows and has worked with the Chair previously) on either a quota or spot price basis or through the logging of private forests. KKI will commence by sourcing timber from private forests as there are numerous landholders and contract loggers to ensure timber supply and mitigate sourcing risk.</p>
    <p>To quantify the direct addressable market KKI conducted extensive market research, contacting 98 stair installers, joineries and furniture manufacturers in addition to wholesalers. Stair installers pay between $XXX and $XXXXm3 with an average of just over $XX00m3 whereas wholesalers buy at around $XX00m3.</p>
    <p>Include Lewis's timber data on stair tread market</p>
  </div>
  <div class="slide-footer">
    <svg width="10" height="10" viewBox="0 0 10 10" aria-hidden="true"><circle cx="5" cy="5" r="4.3" fill="none" stroke="#21ad95" stroke-width="1"/><ellipse cx="5" cy="5" rx="1.8" ry="4.3" fill="none" stroke="#21ad95" stroke-width=".8"/><line x1=".7" y1="5" x2="9.3" y2="5" stroke="#21ad95" stroke-width=".8"/></svg>
    www.websiteaddress.com
  </div>
  <div class="page-num">04</div>
</section>

<p class="board-caption">KARRIDALE KILNS PITCH DECK</p>

</body>
</html>
```